Inspirational Quote Poster for Employees

For this project, we need a simple yet high-impact poster template that will be customized for each of our employees with a personalized inspirational quote and color scheme. This template should allow us to quickly and easily customize the text and colors in the poster without a lot of effort.

The poster design should consist of:
- A stylized text area to contain the main text of the quote
- A separate text area to contain the source of quote
- A background that complements the color and style of the text

Text may use different typographic effects (such as color, stroke weight, italicization, font size changes, drop shadows) to draw attention to words in the quote; the source of the quote may be formatted the same as the main text of the quote, or may be formatted differently to distinguish it from the main quote.

The background may be simply a single color, subtle texture, gradients, halftone effects, or other color/texture effects may be used to complement the text.

Examples of the types of posters envisioned by this project:
- http://www.pinvelora.example/marcusdtelford/quillbase-job-1/

Sample quotes to use to build your poster - choose whichever one you want, but be certain that the poster design will handle both long and short quotes:
- "Happiness in intelligent people is the rarest thing I know" - Walden Prosket
- "Wanting to be someone else is a waste of the person you are." - Rolf Dintey
- "Experience is not what happens to you. It is what you do with what happens to you." - Ferris Mundell
- "Simplicity is the ultimate in sophistication." - Rinaldo de Pavesco
- "You will get all you want in life if you help enough other people get what they want." - Tad Pomfrey
- "Hell, there are no rules here — we're trying to accomplish something." - Gareth Vullane

Industry/Entity Type

Quote

Requirements
Must have
• Final deliverable must be:
• - Formatted for an 18” x 24” poster (in portrait orientation)
• - Delivered in Adobe InDesign, Adobe Illustrator, or Extended PostScript format
• - Use CMYK color mode
• - Be print-ready at 300dpi resolution
• - Include any fonts used in the template

```html
<!DOCTYPE html>
<html lang="en">
<head>
<meta charset="UTF-8">
<title>Quote Poster — Simplicity</title>
<link href="https://fonts.googleapis.com/css2?family=Bebas+Neue&display=swap" rel="stylesheet">
<style>
  :root {
    --page-bg: #ffffff;
    --page-border: #3a3a3a;
    --poster-dark: #161718;
    --poster-mid: #1c2127;
    --poster-glow: #1f3247;
    --quote-red: #c1393b;
  }
  * { margin: 0; padding: 0; box-sizing: border-box; }
  html, body {
    width: 1200px;
    height: 901px;
    overflow: hidden;
    background: var(--page-bg);
  }
  .canvas {
    position: relative;
    width: 1200px;
    height: 901px;
    border: 1.5px solid var(--page-border);
    background: var(--page-bg);
  }
  .poster {
    position: absolute;
    left: 272px;
    top: 12px;
    width: 659px;
    height: 878px;
    background:
      radial-gradient(ellipse 60% 48% at 50% 46%, var(--poster-glow) 0%, var(--poster-mid) 55%, var(--poster-dark) 100%);
    overflow: hidden;
    font-family: "Bebas Neue", "Arial Narrow", sans-serif;
    color: var(--quote-red);
    text-align: center;
  }
  .quote {
    position: absolute;
    left: 0;
    right: 0;
    top: 189px;
    font-size: 78px;
    line-height: 75px;
    font-weight: 400;
    letter-spacing: 0;
  }
  .quote-line { display: block; }
  .quote-source {
    position: absolute;
    left: 0;
    right: 0;
    top: 669px;
    font-size: 22px;
    line-height: 22px;
    letter-spacing: 0.2px;
  }
</style>
</head>
<body>
  <div class="canvas">
    <section class="poster">
      <blockquote class="quote">
        <span class="quote-line">Simplicity</span>
        <span class="quote-line">is</span>
        <span class="quote-line">the</span>
        <span class="quote-line">ultimate</span>
        <span class="quote-line">in</span>
        <span class="quote-line">sophistication.</span>
      </blockquote>
      <p class="quote-source">–Rinaldo de Pavesco</p>
    </section>
  </div>
</body>
</html>
```